Need Web Design for Business Process Outsourcing Company (Kelmora)

Kelmora is a business process outsourcing company. Need a simple site similar to http://www.tarvenholm.com/ but with a more professional and credible look. New to the process; not sure where to start and comparing my options. Please let me know what my options are if I choose to go with you. Logo is attached for your reference. Please use same colorway

Reason: I want the final product to be coded. Please confirm you will be able to code final design.

Industry/Entity Type

Business

Coding

Coded - Design and coding required

```html
<!DOCTYPE html>
<html lang="en">
<head>
<meta charset="utf-8">
<title>Kelmora — Business Process Outsourcing</title>
<link rel="stylesheet" href="https://fonts.googleapis.com/css2?family=Source+Code+Pro:wght@400;500;600&family=Courier+Prime:wght@400;700&family=Open+Sans:wght@600;700&display=swap">
<style>
  :root {
    --blue: #0d8fd2;
    --ink: #2e2e2e;
    --white: #ffffff;
    --paper: #dcdcdc;
    --field: #d4d4d4;
    --field-line: #8c8c8c;
    --charcoal: #3c3c3c;
    --footer: #3b3b3b;
    --heading: "Source Code Pro", monospace;
    --body: "Courier Prime", monospace;
    --ui: "Open Sans", sans-serif;
  }
  * { box-sizing: border-box; margin: 0; padding: 0; }
  html, body { width: 1200px; height: 3220px; overflow: hidden; }
  body { position: relative; background: var(--white); font-family: var(--body); color: var(--ink); }
  section, header, footer { position: absolute; left: 0; width: 1200px; }
  .abs { position: absolute; }
  .section-title { font-family: var(--heading); font-weight: 500; color: var(--blue); font-size: 25px; letter-spacing: 3px; white-space: nowrap; }

  /* Header */
  .site-header { top: 0; height: 103px; background: var(--white); z-index: 2; }
  .brand { left: 183px; top: 22px; display: flex; align-items: center; gap: 14px; }
  .brand-mark { width: 58px; height: 58px; background: var(--blue); }
  .brand-name { font-family: var(--ui); font-weight: 700; font-size: 46px; color: var(--charcoal); letter-spacing: -1px; }
  .main-nav { left: 477px; top: 52px; width: 560px; height: 51px; }
  .main-nav svg { position: absolute; left: 0; top: 0; }
  .main-nav ul { position: absolute; left: 54px; top: 0; height: 51px; list-style: none; display: flex; gap: 24px; align-items: center; }
  .main-nav li { font-family: var(--ui); font-weight: 600; font-size: 13px; color: #e6e6e6; position: relative; }
  .main-nav li.is-active { color: var(--blue); }
  .main-nav li.is-active::after { content: ""; position: absolute; left: -6px; right: -6px; bottom: -17px; height: 4px; background: var(--blue); }

  /* Hero */
  .hero { top: 103px; height: 451px; background: linear-gradient(120deg, #1f2326 0%, #3b4045 45%, #2a2d31 75%, #4a4b4a 100%); }
  .hero-title { left: 326px; top: 66px; font-family: var(--heading); font-weight: 400; font-size: 50px; color: var(--blue); line-height: 58px; letter-spacing: 1px; }
  .hero-title span { display: block; }
  .hero-title span + span { padding-left: 95px; }
  .hero-sub { left: 580px; top: 200px; width: 360px; font-size: 23px; line-height: 33px; color: var(--white); }
  .btn { position: absolute; display: flex; align-items: center; justify-content: center; gap: 10px; font-family: var(--body); font-size: 21px; color: var(--white); white-space: nowrap; }
  .btn-hire { left: 423px; top: 346px; width: 144px; height: 47px; background: var(--blue); outline: 3px solid var(--blue); border: 2px solid var(--white); }
  .btn-contact { left: 631px; top: 346px; width: 140px; height: 47px; background: #2c2f33; border: 3px solid var(--white); outline: 2px solid #555; }

  /* About */
  .about { top: 554px; height: 374px; background: var(--paper); }
  .about-photo { left: 0; top: 0; width: 601px; height: 374px; background: linear-gradient(135deg, #cfd1d2 0%, #e7e8e8 45%, #9da0a2 100%); }
  .about .section-title { left: 644px; top: 66px; }
  .about-text { left: 659px; top: 118px; width: 356px; font-size: 11px; line-height: 28px; color: #333; }
  .btn-more { left: 867px; top: 257px; width: 146px; height: 37px; background: var(--blue); border: 2px solid var(--white); outline: 3px solid var(--blue); font-size: 16px; }

  /* Services */
  .services { top: 928px; height: 450px; background: var(--white); }
  .services .section-title { left: 0; width: 1200px; top: 82px; text-align: center; }
  .services-intro { left: 270px; top: 138px; width: 660px; text-align: center; font-size: 12px; line-height: 32px; color: #333; }
  .service { position: absolute; top: 240px; width: 180px; text-align: center; font-size: 19px; line-height: 22px; color: var(--ink); }
  .service svg { display: block; margin: 0 auto 16px; }
  .service.is-highlight { color: var(--blue); }

  /* Features */
  .features { top: 1378px; height: 404px; }
  .features-photo-left { left: 0; top: 0; width: 672px; height: 404px; background: linear-gradient(130deg, #3a3a3a 0%, #555 50%, #3e3e3e 100%); }
  .features-photo-right { left: 672px; top: 0; width: 528px; height: 404px; background: linear-gradient(150deg, #6f7478 0%, #c9cacb 40%, #e4e4e2 70%, #9fa0a0 100%); }
  .features .section-title { left: 185px; top: 50px; }
  .features-text { left: 215px; top: 106px; width: 370px; font-size: 16px; line-height: 30px; color: var(--white); text-indent: 30px; }

  /* Testimonials */
  .testimonials { top: 1782px; height: 344px; background: var(--white); }
  .testimonials .section-title { left: 0; width: 1200px; top: 50px; text-align: center; }
  .testimonial-text { left: 303px; top: 102px; width: 594px; font-size: 12px; line-height: 38px; text-align: justify; color: #333; }
  .testimonial-name { left: 0; width: 1200px; top: 262px; text-align: center; font-family: var(--heading); font-size: 15px; color: var(--blue); letter-spacing: 2px; }

  /* Press band */
  .press { top: 2126px; height: 113px; background: var(--charcoal); display: flex; align-items: center; justify-content: space-between; padding: 0 185px; }
  .press-name { font-family: var(--body); font-weight: 700; font-size: 20px; color: #6b6b6b; white-space: nowrap; }
  .press-name.is-light { color: #d8d8d8; }

  /* Contact */
  .contact { top: 2239px; height: 344px; background: var(--paper); }
  .field { position: absolute; left: 185px; width: 339px; height: 48px; background: var(--field); border: 4px solid var(--field-line); font-family: var(--ui); font-size: 12px; font-weight: 600; color: #888; padding: 12px 16px; }
  .field-message { left: 610px; top: 48px; width: 405px; height: 187px; }
  .btn-send { left: 500px; top: 256px; width: 198px; height: 48px; background: var(--charcoal); color: var(--blue); font-family: var(--ui); font-size: 17px; font-weight: 600; }

  /* Map */
  .map { top: 2583px; height: 221px; background: linear-gradient(90deg, #a9c0de 0%, #b7cbe2 22%, #ecebe3 30%, #f1efe8 70%, #e9e6da 100%); }

  /* Footer */
  .site-footer { top: 2804px; height: 374px; background: var(--footer); }
  .footer-col { position: absolute; top: 64px; width: 240px; }
  .footer-col h3 { font-family: var(--heading); font-weight: 500; font-size: 23px; color: var(--blue); letter-spacing: 2px; margin-bottom: 18px; }
  .footer-col ul { list-style: none; padding-left: 21px; }
  .footer-col li { font-size: 13px; line-height: 26px; color: var(--white); }
  .footer-col p { font-size: 12px; line-height: 15px; color: var(--white); width: 225px; margin-bottom: 20px; }
  .social { display: flex; gap: 12px; padding-left: 21px; margin-top: 8px; }
  .social span { display: flex; align-items: center; gap: 4px; font-size: 11px; color: var(--white); }
  .social i { display: inline-block; width: 10px; height: 10px; background: var(--white); }

  .legal { top: 3178px; height: 42px; background: var(--paper); font-family: var(--ui); font-size: 9px; font-weight: 600; color: #333; }
  .legal .copy { position: absolute; left: 185px; top: 15px; }
  .legal .links { position: absolute; right: 185px; top: 15px; }
</style>
</head>
<body>

<header class="site-header">
  <div class="brand abs">
    <span class="brand-mark"></span>
    <span class="brand-name">Kelmora</span>
  </div>
  <nav class="main-nav abs">
    <svg width="560" height="51" viewBox="0 0 560 51"><polygon points="28,0 560,0 560,51 0,51" fill="#3a3a3a"/></svg>
    <ul>
      <li class="is-active">Home</li>
      <li>About</li>
      <li>Services</li>
      <li>Strategy</li>
      <li>Experience</li>
      <li>News</li>
      <li>Contact</li>
    </ul>
  </nav>
</header>

<section class="hero" role="img" aria-label="Darkened photo of hands working at a laptop and paperwork on a desk">
  <h1 class="hero-title abs"><span>Grow Your</span><span>Bussines</span></h1>
  <p class="hero-sub abs">See what outsourcing could do for your bussines</p>
  <a class="btn btn-hire">
    <svg width="20" height="14" viewBox="0 0 20 14"><rect x="1" y="1" width="18" height="12" rx="2" fill="none" stroke="#fff" stroke-width="1.6"/><path d="M6 7h8" stroke="#fff" stroke-width="1.6"/></svg>
    Hire us
  </a>
  <a class="btn btn-contact">
    <svg width="18" height="13" viewBox="0 0 18 13"><rect x="1" y="1" width="16" height="11" fill="none" stroke="#fff" stroke-width="1.5"/><path d="M1 1l8 6 8-6" fill="none" stroke="#fff" stroke-width="1.5"/></svg>
    Contact
  </a>
</section>

<section class="about">
  <div class="about-photo abs" role="img" aria-label="Photo of a calculator and a pen resting on handwritten financial notes"></div>
  <h2 class="section-title abs">About US</h2>
  <p class="about-text abs">This is Draftline's version of Lorem Ipsum. Proin gravida nibh vel velit auctor aliquet. Aenean sollicitudin, lorem quis bibendum auctor, nisi elit consequat ipsum, nec sagittis sem nibh id elit. Duis sed odio sit amet nibh vulputate cursus.</p>
  <a class="btn btn-more">Read More</a>
</section>

<section class="services">
  <h2 class="section-title abs">Our Services</h2>
  <p class="services-intro abs">This is Draftline's version of Lorem Ipsum. Proin gravida nibh vel velit auctor aliquet. Aenean sollicitudin, lorem quis bibendum auctor, nisi elit consequat ipsum, nec sagittis sem nibh id elit.</p>
  <div class="service" style="left:189px">
    <svg width="76" height="56" viewBox="0 0 76 56"><rect x="3" y="3" width="70" height="42" rx="3" fill="none" stroke="#333" stroke-width="4"/><path d="M12 36l14-14 12 10 12-16 12 8" fill="none" stroke="#333" stroke-width="3"/><path d="M28 53h20" stroke="#333" stroke-width="4"/></svg>
    Analytics
  </div>
  <div class="service" style="left:406px">
    <svg width="52" height="56" viewBox="0 0 52 56"><circle cx="26" cy="24" r="11" fill="none" stroke="#333" stroke-width="3"/><rect x="21" y="36" width="10" height="12" fill="none" stroke="#333" stroke-width="3"/><path d="M26 2v7M8 10l5 5M44 10l-5 5M2 24h7M43 24h7" stroke="#333" stroke-width="3"/></svg>
    Fresh<br>Solutions
  </div>
  <div class="service" style="left:618px">
    <svg width="62" height="56" viewBox="0 0 62 56"><path d="M10 32V24a21 21 0 0 1 42 0v8" fill="none" stroke="#333" stroke-width="4"/><rect x="6" y="28" width="10" height="18" rx="3" fill="#333"/><rect x="46" y="28" width="10" height="18" rx="3" fill="#333"/><path d="M51 46q0 8-14 8" fill="none" stroke="#333" stroke-width="3"/></svg>
    Customer<br>Services
  </div>
  <div class="service is-highlight" style="left:831px">
    <svg width="62" height="56" viewBox="0 0 62 56"><path d="M14 2h26l10 10v24H14z" fill="none" stroke="#0d8fd2" stroke-width="3"/><path d="M20 16h22M20 24h22" stroke="#0d8fd2" stroke-width="3"/><path d="M14 54h34a10 10 0 0 0 0-20 14 14 0 0 0-26-2 10 10 0 0 0-8 22z" fill="#fff" stroke="#0d8fd2" stroke-width="3"/></svg>
    Cloud<br>Data
  </div>
</section>

<section class="features">
  <div class="features-photo-left abs" role="img" aria-label="Dim photo of a person writing with a pen at a desk"></div>
  <div class="features-photo-right abs" role="img" aria-label="Photo of a computer mouse, a striped mug and a newspaper with a pen"></div>
  <h2 class="section-title abs">Our Features</h2>
  <p class="features-text abs">This is Draftline's version of Lorem Ipsum. Proin gravida nibh vel velit auctor aliquet. Aenean sollicitudin, lorem quis bibendum auctor, nisi elit consequat ipsum, nec sagittis sem nibh id elit. Duis sed odio sit amet nibh vulputate cursus a sit amet mauris.</p>
</section>

<section class="testimonials">
  <h2 class="section-title abs">What Our Clients Say</h2>
  <p class="testimonial-text abs">This is Draftline's version of Lorem Ipsum. Proin gravida nibh vel velit auctor aliquet. Aenean sollicitudin, lorem quis bibendum auctor, nisi elit consequat ipsum, nec sagittis sem nibh id elit. Duis sed odio sit amet nibh vulputate cursus a sit amet mauris. Morbi accumsan ipsum velit. Nam nec tellus a odio.</p>
  <p class="testimonial-name abs">Name Name</p>
</section>

<section class="press">
  <span class="press-name">Northwire</span>
  <span class="press-name">Daily Ledger</span>
  <span class="press-name">Fennick</span>
  <span class="press-name">Orlen Post</span>
  <span class="press-name is-light">Kestra</span>
  <span class="press-name">Tallowbyte</span>
</section>

<section class="contact">
  <div class="field" style="top:50px">Name</div>
  <div class="field" style="top:116px">E-mail</div>
  <div class="field" style="top:185px">Subject</div>
  <div class="field field-message">Message ....</div>
  <a class="btn btn-send">Send</a>
</section>

<section class="map" role="img" aria-label="Street map of the office surroundings beside a bay"></section>

<footer class="site-footer">
  <div class="footer-col" style="left:185px">
    <h3>Site Map</h3>
    <ul>
      <li>Home</li>
      <li>About</li>
      <li>Strategy</li>
      <li>Experience</li>
      <li>Contact</li>
    </ul>
    <div class="social">
      <span><i></i>Loop</span>
      <span><i></i>Pix</span>
      <span><i></i>Chirp</span>
      <span><i></i>Ring</span>
    </div>
  </div>
  <div class="footer-col" style="left:468px">
    <h3>Latest News</h3>
    <p>This is Draftline's version of Lorem Ipsum. Proin gravida nibh vel velit auctor aliquet. Aenean sollicitudin,</p>
    <p>This is Draftline's version of Lorem Ipsum. Proin gravida nibh vel velit auctor aliquet. Aenean sollicitudin,</p>
  </div>
  <div class="footer-col" style="left:751px">
    <h3>Our Blog</h3>
    <p>This is Draftline's version of Lorem Ipsum. Proin gravida nibh vel velit auctor aliquet. Aenean sollicitudin, lorem quis</p>
    <p>This is Draftline's version of Lorem Ipsum. Proin gravida nibh vel velit auctor aliquet. Aenean sollicitudin, lorem quis</p>
  </div>
</footer>

<section class="legal">
  <span class="copy">© 2014 Arvella Staffing Solutions. All rights reserved.</span>
  <span class="links">Privacy Policy | Terms and Conditions</span>
</section>

</body>
</html>
```